We are a General Practice - Family medicine
We also have Allied Health professionals working within our team

Industry/Entity Type

Business

Contact Information for Business Card

Front of the card to display:

HARBOURVIEW MEDICAL
PHONE 6381 2947

5/14 Kellerton Avenue
Launceston Tasmania 7268

Back of the card to display:

My Appointments
Date:
Time:
With:

Please remember to phone us on 6381 2947 to cancel your appointment if you can't keep it.
A fee applied to missed appointments

```html
<!DOCTYPE html>
<html lang="en">
<head>
<meta charset="utf-8">
<title>Harbourview Medical – Business Cards</title>
<link href="https://fonts.googleapis.com/css2?family=Cinzel:wght@400&family=Open+Sans:wght@400;600&family=Open+Sans+Condensed:wght@700&display=swap" rel="stylesheet">
<style>
  :root {
    --bg: #e4e4e4;
    --card: #ffffff;
    --brand-blue: #2f8fd0;
    --band-blue: #2a87cc;
    --band-blue-dark: #1f72b6;
    --leaf-green: #6cb33f;
    --ink: #4a4a4a;
    --rule: #9a9a9a;
  }
  * { box-sizing: border-box; margin: 0; padding: 0; }
  html, body { width: 1200px; height: 852px; overflow: hidden; }
  body {
    background: var(--bg);
    font-family: "Open Sans", Arial, sans-serif;
    color: var(--ink);
    position: relative;
  }
  .card {
    position: absolute;
    width: 560px;
    height: 320px;
    background: var(--card);
    border-radius: 22px;
    overflow: hidden;
    box-shadow: 0 2px 6px rgba(0,0,0,.12);
  }
  .card--appointment { left: 320px; top: 70px; }
  .card--contact { left: 320px; top: 462px; }

  .brand {
    position: absolute;
    display: flex;
    align-items: center;
    gap: 12px;
  }
  .brand__dot {
    width: 34px; height: 34px;
    border-radius: 50%;
    background: var(--brand-blue);
  }
  .brand__name {
    font-family: "Open Sans", Arial, sans-serif;
    font-weight: 600;
    font-size: 34px;
    color: var(--brand-blue);
    letter-spacing: -0.5px;
  }

  /* Appointment card */
  .card--appointment .brand { left: 96px; top: 30px; }
  .appointments__title {
    position: absolute;
    left: 0; right: 0; top: 100px;
    text-align: center;
    font-family: "Cinzel", Georgia, serif;
    font-size: 17px;
    letter-spacing: 1.5px;
    color: #444;
  }
  .field {
    position: absolute;
    display: flex;
    align-items: flex-end;
    font-size: 13px;
    color: #555;
  }
  .field__line {
    flex: 1;
    border-bottom: 1px solid var(--rule);
    margin-left: 6px;
    height: 14px;
  }
  .field--time { left: 300px; right: 36px; top: 142px; }
  .field--with { left: 36px; right: 36px; top: 184px; }
  .field--date { left: 36px; right: 36px; top: 226px; }
  .blank-rule {
    position: absolute;
    left: 36px; width: 230px; top: 156px;
    border-bottom: 1px solid var(--rule);
  }
  .notice {
    position: absolute;
    left: 0; right: 0; bottom: 0;
    height: 60px;
    background: linear-gradient(180deg, var(--band-blue), var(--band-blue-dark));
    color: #fff;
    text-align: center;
    font-family: "Open Sans Condensed", "Arial Narrow", sans-serif;
    font-weight: 700;
    font-size: 13px;
    line-height: 18px;
    padding-top: 12px;
  }
  .notice__fee { text-transform: uppercase; font-size: 12px; }

  /* Contact card */
  .contact__band {
    position: absolute;
    left: 0; top: 0; bottom: 0;
    width: 64px;
    background: linear-gradient(180deg, var(--band-blue), var(--band-blue-dark));
    border-right: 6px solid var(--leaf-green);
  }
  .card--contact .brand { left: 100px; top: 34px; }
  .person { position: absolute; left: 100px; top: 128px; }
  .person__name {
    font-weight: 600;
    font-size: 24px;
    color: var(--brand-blue);
    line-height: 1.1;
  }
  .person__title { font-size: 13px; color: #555; margin-top: 4px; }
  .details {
    position: absolute;
    left: 100px; top: 198px;
    list-style: none;
    font-size: 14px;
    color: #555;
  }
  .details li {
    display: flex;
    align-items: center;
    gap: 10px;
    height: 22px;
  }
  .details svg { width: 14px; height: 14px; fill: var(--brand-blue); }
  .details__address { padding-left: 24px; margin-top: 4px; }
</style>
</head>
<body>

<section class="card card--appointment">
  <div class="brand">
    <span class="brand__dot"></span>
    <span class="brand__name">Harbourview Medical</span>
  </div>
  <h2 class="appointments__title">MY APPOINTMENTS</h2>
  <div class="blank-rule"></div>
  <div class="field field--time"><span>Time:</span><span class="field__line"></span></div>
  <div class="field field--with"><span>With:</span><span class="field__line"></span></div>
  <div class="field field--date"><span>Date:</span><span class="field__line"></span></div>
  <div class="notice">
    <p>Please remember to phone us on 6381 2947 to cancel your appointment if you can't keep it.</p>
    <p class="notice__fee">A fee applied to missed appointments</p>
  </div>
</section>

<section class="card card--contact">
  <div class="contact__band"></div>
  <div class="brand">
    <span class="brand__dot"></span>
    <span class="brand__name">Harbourview Medical</span>
  </div>
  <div class="person">
    <p class="person__name">Your name</p>
    <p class="person__title">Your Title</p>
  </div>
  <ul class="details">
    <li>
      <svg viewBox="0 0 16 16" aria-hidden="true"><path d="M3 1h3l1.5 4-2 1.2a9 9 0 0 0 4.3 4.3L11 8.5l4 1.5v3a2 2 0 0 1-2 2A12 12 0 0 1 1 3a2 2 0 0 1 2-2z"/></svg>
      <span>6381 2947</span>
    </li>
    <li>
      <svg viewBox="0 0 16 16" aria-hidden="true"><path d="M1 3h14v10H1z M2 4l6 5 6-5" fill="none" stroke="#2f8fd0" stroke-width="1.6"/></svg>
      <span>reception@harbourviewmed.com.au</span>
    </li>
    <li>
      <svg viewBox="0 0 16 16" aria-hidden="true"><circle cx="8" cy="8" r="6.5" fill="none" stroke="#2f8fd0" stroke-width="1.4"/><path d="M1.5 8h13M8 1.5c-3 3.5-3 9.5 0 13M8 1.5c3 3.5 3 9.5 0 13" fill="none" stroke="#2f8fd0" stroke-width="1.2"/></svg>
      <span>www.harbourviewmed.com.au</span>
    </li>
    <li class="details__address">5/14 Kellerton Avenue Launceston Tasmania 7268</li>
  </ul>
</section>

</body>
</html>
```